Hollowmere Farm Promotional Leaflet

The team at Hollowmere Farm can help with every aspect of managing and enhancing your home from housekeeping and professional cleaning, laundry and ironing to providing chic and contemporary flower arrangements and even food for your pets!We take pride in providing high-end, consistent and reliable professional services bespoke to you. Whether you are a busy professional working long hours, a stay-at home parent or retired; having professional help in the home gives you time to spend on the things you enjoy.We are providing a very upmarket, highly professional service and need an A5 promotional leaflet to be designed. Please refer to www.hollowmerefarm.example.co.uk and see the section on 'Home Management'The leaflet should incorporate the Hollowmere Farm logo without the 'tipi', and any suitable photography images used on the home page of the website or the 'home management' section.

Target Market(s)

high-end, affluent owners of luxury homes

Industry/Entity Type

Farm

Contact Information for Business Card

The business card design needs to be suitable for use across all of Hollowmere Farm businesses, specifically:
Hollowmere Farm Home Management - otherwise known as Hollowmere Farm @ Home (this uses the typographical logo
Hollowmere Farm Weddings & Events - this uses the 'tipi' logo

Requirements
Must have
• Design in keeping with the look and feel of the logo and website design
• www.hollowmerefarm.example.co.uk

```html
<!DOCTYPE html>
<html lang="en">
<head>
<meta charset="utf-8">
<title>Hollowmere Farm Business Card</title>
<link rel="stylesheet" href="https://fonts.googleapis.com/css2?family=Open+Sans:wght@400;600&display=swap">
<style>
  :root {
    --backdrop: #3b3430;
    --card: #141414;
    --card-edge: #0c0c0c;
    --pink: #d4245f;
    --gold: #c9a25a;
    --white: #f2f2f2;
    --muted: #bdbdbd;
  }
  * { margin: 0; padding: 0; box-sizing: border-box; }
  html, body {
    width: 1200px; height: 864px; overflow: hidden;
    background: var(--backdrop);
    font-family: "Open Sans", Arial, sans-serif;
  }
  .stage {
    position: relative; width: 1200px; height: 864px;
    display: flex; align-items: center; justify-content: center; gap: 40px;
  }
  .card {
    position: relative; width: 540px; height: 309px;
    background: var(--card);
    border: 1px solid var(--card-edge);
    box-shadow: 0 14px 30px rgba(0,0,0,.45);
    overflow: hidden;
  }
  .card-back .texture {
    position: absolute; inset: 0;
    background: radial-gradient(ellipse at 50% 45%, #1d1d1d 0%, #141414 70%);
  }
  .wordmark {
    font-weight: 600; color: var(--pink);
    letter-spacing: .5px; white-space: nowrap;
    display: flex; align-items: center; gap: 10px;
  }
  .wordmark .dot {
    width: 12px; height: 12px; border-radius: 50%; background: var(--gold);
  }
  .card-back .wordmark {
    position: absolute; left: 90px; top: 100px; font-size: 34px;
  }
  .card-back .site {
    position: absolute; left: 90px; top: 196px;
    font-size: 13px; letter-spacing: 3px; color: var(--muted);
  }
  .card-front .wordmark {
    position: absolute; right: 40px; top: 82px; font-size: 34px;
  }
  .person {
    position: absolute; right: 318px; top: 178px; text-align: right;
  }
  .person .name { color: var(--pink); font-weight: 600; font-size: 14px; letter-spacing: .5px; }
  .person .role { color: var(--gold); font-size: 14px; margin-top: 2px; }
  .divider {
    position: absolute; left: 238px; top: 170px; width: 1px; height: 110px;
    background: linear-gradient(to bottom, rgba(255,255,255,.9), rgba(255,255,255,.1));
  }
  .contact {
    position: absolute; left: 256px; top: 172px;
    color: var(--white); font-size: 14px; line-height: 20px;
    list-style: none;
  }
  .contact li { display: flex; align-items: center; gap: 7px; }
  .contact svg { width: 12px; height: 12px; fill: var(--pink); flex: none; }
</style>
</head>
<body>
<main class="stage">
  <section class="card card-back">
    <div class="texture" role="img" aria-label="Faint tone-on-tone brand pattern across the card back"></div>
    <div class="wordmark"><span class="dot"></span>Hollowmere Farm</div>
    <p class="site">www.hollowmerefarm.example.co.uk</p>
  </section>

  <section class="card card-front">
    <div class="wordmark"><span class="dot"></span>Hollowmere Farm</div>
    <div class="person">
      <p class="name">DANIEL AVERY</p>
      <p class="role">CEO/FOUNDER</p>
    </div>
    <div class="divider"></div>
    <ul class="contact">
      <li>Hollowmere Farm</li>
      <li>Mill Lane, Ashcombe</li>
      <li>Somerset TA00 0XX, GB</li>
      <li>
        <svg viewBox="0 0 24 24" aria-hidden="true"><path d="M6.6 10.8a15.1 15.1 0 0 0 6.6 6.6l2.2-2.2a1 1 0 0 1 1-.25 11.4 11.4 0 0 0 3.6.57 1 1 0 0 1 1 1V20a1 1 0 0 1-1 1A17 17 0 0 1 3 4a1 1 0 0 1 1-1h3.5a1 1 0 0 1 1 1c0 1.25.2 2.45.57 3.6a1 1 0 0 1-.25 1z"/></svg>
        +44 7000 123456
      </li>
      <li>
        <svg viewBox="0 0 24 24" aria-hidden="true"><circle cx="12" cy="12" r="10"/><path d="M2 12h20M12 2c3 3 3 17 0 20M12 2c-3 3-3 17 0 20" stroke="#141414" stroke-width="1.6" fill="none"/></svg>
        www.hollowmerefarm.example.co.uk
      </li>
    </ul>
  </section>
</main>
</body>
</html>
```